Global Leadership Company requires banner design

I need 3 large banners designed. i will be using these for advertising and also a condensed version as the header on a splash pages.

I have attached the wording and also the photo's that i'd like used in each design.
Note: i've just placed the wording randomly, you'll have to place it where it makes the most sense for the message and the design.

I want something with bright colors that pops.

Reason: I'd like to give the most recent designers time to submit quality work.

```html
<!DOCTYPE html>
<html lang="en">
<head>
<meta charset="utf-8">
<title>Personal Empowerment Banner</title>
<link rel="stylesheet" href="https://fonts.googleapis.com/css2?family=Montserrat:ital,wght@0,300;0,400;0,500;0,800;1,400&family=Kalam:wght@400&display=swap">
<style>
  :root {
    --navy: #1c2b5e;
    --orange: #ee9c3c;
    --orange-bright: #f3a536;
    --white: #ffffff;
    --button-blue: #2a7fe3;
    --script-red: #c5271e;
    --portrait-ring: #f8cfa0;
    --divider: rgba(255, 255, 255, 0.75);
  }
  * { margin: 0; padding: 0; box-sizing: border-box; }
  html, body { width: 1200px; height: 360px; overflow: hidden; background: var(--white); }
  .banner {
    position: relative;
    width: 1200px;
    height: 360px;
    overflow: hidden;
    font-family: "Montserrat", Arial, sans-serif;
    background: var(--orange);
  }
  .hero-photo {
    position: absolute;
    left: 0; top: 0;
    width: 357px; height: 360px;
    background: linear-gradient(180deg, #2d4b86 0%, #5876a8 35%, #8c6b8a 55%, #e0502a 75%, #f7a02c 88%, #2a1a14 100%);
  }
  .panel-divider {
    position: absolute;
    left: 357px; top: 0;
    width: 1px; height: 360px;
    background: var(--divider);
  }
  .headline-band {
    position: absolute;
    left: 358px; top: 0;
    width: 842px; height: 94px;
    background: var(--navy);
    border-bottom: 1px solid var(--divider);
  }
  .wanted {
    position: absolute;
    left: 62px; top: 14px;
    font-weight: 800;
    font-size: 58px;
    letter-spacing: 0.5px;
    color: var(--orange-bright);
    line-height: 1;
  }
  .wanted-sub {
    position: absolute;
    left: 387px; top: 20px;
    font-weight: 300;
    font-size: 22px;
    line-height: 26px;
    color: var(--white);
  }
  .title {
    position: absolute;
    left: 388px; top: 108px;
    font-weight: 300;
    font-size: 42px;
    color: var(--navy);
    line-height: 1.1;
  }
  .subtitle {
    position: absolute;
    left: 532px; top: 160px;
    font-weight: 400;
    font-size: 29px;
    color: var(--white);
    line-height: 1.1;
  }
  .cta {
    position: absolute;
    left: 1036px; top: 134px;
    width: 136px; height: 49px;
    border: 3px solid #fbe3c4;
    border-radius: 8px;
    background: var(--button-blue);
    color: var(--white);
    font-size: 16px;
    font-weight: 400;
    display: flex; align-items: center; justify-content: center;
    text-decoration: none;
  }
  .portrait {
    position: absolute;
    left: 391px; top: 222px;
    width: 122px; height: 122px;
    border-radius: 50%;
    border: 4px solid var(--portrait-ring);
    background: radial-gradient(circle at 50% 55%, #e9b58f 0%, #d8a070 35%, #b04fa8 75%, #6d2b8a 100%);
  }
  .benefits {
    position: absolute;
    left: 549px; top: 233px;
    list-style: none;
    font-size: 13px;
    line-height: 20.5px;
    color: var(--navy);
  }
  .dashed-rule {
    position: absolute;
    top: 236px;
    height: 90px;
    border-left: 1px dashed rgba(255, 255, 255, 0.85);
  }
  .rule-one { left: 760px; }
  .rule-two { left: 1024px; }
  .testimonial {
    position: absolute;
    left: 782px; top: 236px;
    width: 220px;
    color: var(--navy);
  }
  .testimonial blockquote {
    position: relative;
    padding-left: 15px;
    font-size: 12.5px;
    line-height: 20px;
  }
  .quote-mark {
    font-family: Georgia, serif;
    font-size: 20px;
    line-height: 0;
    position: relative;
    top: 4px;
  }
  .quote-open { position: absolute; left: 0; top: 10px; }
  .testimonial cite {
    display: block;
    margin-top: 10px;
    padding-left: 15px;
    font-style: italic;
    font-size: 13px;
  }
  .launch-note {
    position: absolute;
    left: 1050px; top: 250px;
    font-family: "Kalam", cursive;
    font-size: 15px;
    line-height: 25px;
    color: var(--script-red);
  }
</style>
</head>
<body>
  <div class="banner">
    <div class="hero-photo" role="img" aria-label="Silhouette of a person standing on a rock with arms raised against a vivid sunset sky"></div>
    <div class="panel-divider"></div>

    <header class="headline-band">
      <h1 class="wanted">WANTED</h1>
      <p class="wanted-sub">Driven individuals READY to take<br>their results to the next level</p>
    </header>

    <h2 class="title">Personal Empowerment.....</h2>
    <p class="subtitle">the NEXT Big Business Boom!</p>
    <a class="cta" href="#">Learn more</a>

    <div class="portrait" role="img" aria-label="Portrait photo of a smiling woman giving the testimonial"></div>

    <ul class="benefits">
      <li>Make up to $5,000 per sale</li>
      <li>No cold calling</li>
      <li>No experience required</li>
      <li>No pressure selling</li>
      <li>NOT MLM</li>
    </ul>

    <div class="dashed-rule rule-one"></div>

    <figure class="testimonial">
      <blockquote>
        <span class="quote-mark quote-open">&ldquo;</span>Within just 5 months I was making over $25,000/month <span class="quote-mark">&rdquo;</span>
      </blockquote>
      <cite>Dana, Colorado</cite>
    </figure>

    <div class="dashed-rule rule-two"></div>

    <p class="launch-note">Just launched in<br>United States</p>
  </div>
</body>
</html>
```